Want to market to schools to offer free chair massages for teacher and staff of the schools

This postcard will be mailed to all public schools in the U.S.

We want the schools to call our company to have a massage therapist provide free chair massages to the teachers and staff at their next School Improvement or Teacher Institute day.

want to make the postcard fun and inviting.

The postcard is 4 1/4" X 6"

FRONT AND BACK DESIGN.

For the back of postcard design, I have attached a template. You can use all the space except where the return label and stamp will go.

Target Market(s)

Target is schools and teachers

Industry/Entity Type

Teacher

```html
<!DOCTYPE html>
<html lang="en">
<head>
<meta charset="utf-8">
<title>Free Chair Massage for Teacher Institute Day</title>
<link rel="stylesheet" href="https://fonts.googleapis.com/css2?family=EB+Garamond:wght@500;800&family=Libre+Baskerville:wght@700&family=Carlito:wght@400;700&display=swap">
<style>
  :root {
    --paper: #ffffff;
    --ink: #111111;
    --brand-grey: #4a5563;
    --brand-green: #6fae3a;
    --skin-light: #e9c7ae;
    --skin-mid: #c99474;
    --skin-dark: #8a5a3f;
  }
  * { margin: 0; padding: 0; box-sizing: border-box; }
  html, body { width: 1200px; height: 802px; overflow: hidden; background: var(--paper); }
  .postcard { position: relative; width: 1200px; height: 802px; background: var(--paper); color: var(--ink); }

  .brand { position: absolute; left: 49px; top: 96px; display: flex; align-items: center; gap: 14px; }
  .brand-dot { width: 88px; height: 88px; border-radius: 50%; background: var(--brand-green); }
  .brand-name { font-family: "Carlito", sans-serif; font-weight: 400; color: var(--brand-grey); font-size: 36px; line-height: 1.05; }

  .headline { position: absolute; left: 447px; top: 30px; width: 700px;
    font-family: "EB Garamond", serif; font-weight: 500; font-size: 39px; line-height: 70px; }
  .tagline { position: absolute; left: 448px; top: 178px; width: 630px; text-align: center;
    font-family: "EB Garamond", serif; font-weight: 800; font-size: 44px; letter-spacing: 1px; }

  .photo { position: absolute; left: 37px; top: 292px; width: 382px; height: 479px;
    background: radial-gradient(ellipse at 55% 45%, var(--skin-light) 0%, var(--skin-mid) 55%, var(--skin-dark) 100%); }

  .testimonial { position: absolute; left: 520px; top: 326px; width: 520px;
    font-family: "Libre Baskerville", serif; font-weight: 700; font-size: 20px; line-height: 43px; }
  .testimonial cite { display: block; font-style: normal; padding-left: 14px; }

  .call-to-action { position: absolute; left: 706px; top: 672px; width: 440px;
    font-family: "Carlito", sans-serif; font-weight: 700; font-size: 22px; line-height: 29px; text-transform: uppercase; }
</style>
</head>
<body>
<main class="postcard">
  <div class="brand">
    <span class="brand-dot"></span>
    <span class="brand-name">VitalPath<br>Wellness Centers</span>
  </div>

  <h1 class="headline">Free Chair Massage at your next School<br>Improvement &amp; Teacher Institute Day.</h1>
  <p class="tagline">FREE AND FUN</p>

  <div class="photo" role="img" aria-label="Photo of a man seen from behind, rubbing his sore neck and shoulder"></div>

  <blockquote class="testimonial">
    <p>Testimonial:</p>
    <p>“ Each teacher was delighted to participate and couldn’t believe the difference 10 minutes in a massage chair made”</p>
    <cite>–Marisol</cite>
  </blockquote>

  <p class="call-to-action">Call today to reserve&nbsp; a date for your school<br>1-800-555-0142</p>
</main>
</body>
</html>
```